BrambleWorks business card

Looking for business card design that supports our company/software values. We have 2 logo designs at the moment but open to change if you think you can enhance the brand. Check out website www.brambleworks.com.au.

Target Market(s)

Education

Contact Information for Business Card

Name, title, mobile, email and website

Font styles to use
Sans Serif

Colors

Designer to choose colors to be used in the design.

Requirements
Must have
• BrambleWorks logo with tree and tagline on rear side with dark grey background colour

```html
<!DOCTYPE html>
<html lang="en">
<head>
<meta charset="utf-8">
<title>BrambleWorks business card</title>
<link rel="stylesheet" href="https://fonts.googleapis.com/css2?family=Ubuntu:wght@400;500;700&display=swap">
<style>
  :root {
    --backdrop: #ececec;
    --card-light: #ffffff;
    --card-dark: #4e504d;
    --ink: #4a4b4a;
    --ink-soft: #5a5b5a;
    --leaf: #4f7f38;
    --rule: #c9c9c9;
    --paper: #ffffff;
  }
  * { margin: 0; padding: 0; box-sizing: border-box; }
  html, body { width: 1200px; height: 1200px; overflow: hidden; }
  body {
    background: var(--backdrop);
    font-family: "Ubuntu", sans-serif;
    position: relative;
  }
  .card {
    position: absolute;
    border-radius: 10px;
    box-shadow: 0 6px 14px rgba(0,0,0,0.18);
  }
  .card-front {
    left: 104px; top: 275px; width: 354px; height: 619px;
    background: var(--card-light);
    color: var(--ink);
  }
  .brand-mark {
    position: absolute; left: 0; right: 0; top: 470px;
    display: flex; align-items: center; justify-content: center; gap: 10px;
  }
  .card-front .brand-mark { top: 182px; }
  .brand-dot { width: 22px; height: 22px; border-radius: 50%; background: var(--leaf); }
  .brand-name-front { font-size: 30px; font-weight: 500; color: var(--ink); }
  .person {
    position: absolute; left: 0; right: 0; top: 426px; text-align: center;
  }
  .person-name { font-size: 26px; font-weight: 700; color: var(--ink); line-height: 1.1; }
  .person-title { font-size: 14.5px; color: var(--ink-soft); letter-spacing: 0.5px; margin-top: 2px; }
  .icon-row {
    position: absolute; left: 91px; width: 172px; top: 483px;
    display: flex; align-items: center; gap: 3px;
  }
  .icon-row .rule { flex: 1; height: 1px; background: var(--rule); }
  .icon { width: 22px; height: 22px; border-radius: 50%; background: var(--leaf); display: flex; align-items: center; justify-content: center; }
  .icon svg { width: 12px; height: 12px; }
  .contact {
    position: absolute; left: 0; right: 0; top: 509px; text-align: center;
    font-size: 14px; letter-spacing: 0.8px; color: var(--ink); line-height: 20px;
  }
  .card-back {
    left: 489px; top: 541px; width: 619px; height: 353px;
    background: var(--card-dark);
    overflow: hidden;
  }
  .backdrop-circle {
    position: absolute; left: 60px; top: 90px; width: 300px; height: 300px;
    border-radius: 50%; background: rgba(255,255,255,0.035);
  }
  .lockup {
    position: absolute; left: 0; right: 0; top: 132px;
    display: flex; align-items: center; justify-content: center; gap: 16px;
  }
  .lockup .brand-dot { width: 54px; height: 54px; background: var(--paper); }
  .wordmark { color: var(--paper); }
  .wordmark-name { font-size: 42px; font-weight: 500; line-height: 1; padding-bottom: 8px; border-bottom: 1.5px solid var(--paper); }
  .wordmark-tagline { font-size: 18px; font-weight: 500; margin-top: 6px; text-align: center; }
</style>
</head>
<body>
  <section class="card card-front">
    <div class="brand-mark">
      <span class="brand-dot"></span>
      <span class="brand-name-front">BrambleWorks</span>
    </div>
    <div class="person">
      <p class="person-name">Daniel Hartley</p>
      <p class="person-title">Founder and CEO</p>
    </div>
    <div class="icon-row">
      <span class="rule"></span>
      <span class="icon" aria-label="Phone">
        <svg viewBox="0 0 24 24"><path fill="#fff" d="M6.6 10.8a15.1 15.1 0 0 0 6.6 6.6l2.2-2.2c.3-.3.7-.4 1-.2 1.1.4 2.3.6 3.6.6.6 0 1 .4 1 1V20c0 .6-.4 1-1 1C10.6 21 3 13.4 3 4c0-.6.4-1 1-1h3.5c.6 0 1 .4 1 1 0 1.3.2 2.5.6 3.6.1.3 0 .7-.2 1z"/></svg>
      </span>
      <span class="icon" aria-label="Email">
        <svg viewBox="0 0 24 24"><path fill="#fff" d="M2 5h20v14H2z"/><path fill="none" stroke="#4f7f38" stroke-width="2" d="M2 6l10 7 10-7"/></svg>
      </span>
      <span class="icon" aria-label="Website">
        <svg viewBox="0 0 24 24" fill="none" stroke="#fff" stroke-width="1.8"><circle cx="12" cy="12" r="9.5"/><ellipse cx="12" cy="12" rx="4" ry="9.5"/><path d="M2.5 12h19M4 7h16M4 17h16"/></svg>
      </span>
      <span class="rule"></span>
    </div>
    <div class="contact">
      <p>000 000 0000</p>
      <p>info@brambleworks.com.au</p>
      <p>www.brambleworks.com.au</p>
    </div>
  </section>

  <section class="card card-back">
    <span class="backdrop-circle"></span>
    <div class="lockup">
      <span class="brand-dot"></span>
      <div class="wordmark">
        <p class="wordmark-name">BrambleWorks</p>
        <p class="wordmark-tagline">Student Success Platform</p>
      </div>
    </div>
  </section>
</body>
</html>
```